Company PowerPoint Presentation Template

I am looking for a business powerpoint template tailored to my company that specializes in permafrost services for the mining, transportation, and oil & gas industries. The template would be used to present project findings from studies completed for our clients. I am looking for a crisp, technical, professional business look to the template. Our business is located in North America and English is the primary language used to communicate our work. Complimentary colors associated with the business is blue (RGB, 0,112,192) or something similar in color.

```html
<!DOCTYPE html>
<html lang="en">
<head>
<meta charset="utf-8">
<title>Borealis Frostline Consulting – Presentation Template</title>
<link href="https://fonts.googleapis.com/css2?family=Michroma&family=Roboto:wght@400;500;700&display=swap" rel="stylesheet">
<style>
:root{
  --brand:#0b6cc4;
  --brand-deep:#0a4f96;
  --brand-soft:#cfe2f5;
  --ink:#151c2c;
  --text:#2b2f36;
  --muted:#6c6f75;
  --canvas:#d5d5d5;
  --white:#ffffff;
  --panel:#f0f0f0;
}
*{box-sizing:border-box;margin:0;padding:0}
html,body{width:1200px;height:4043px;overflow:hidden}
body{background:linear-gradient(180deg,#d9d9d9,#cfcfcf);font-family:"Roboto",Arial,sans-serif;color:var(--text);position:relative}
.slide{position:absolute;left:83px;width:1034px;height:580px;background:var(--white);overflow:hidden;box-shadow:0 6px 18px rgba(0,0,0,.12)}
.abs{position:absolute}
.photo{position:absolute}
.brand{position:absolute;font-family:"Michroma",sans-serif;color:var(--ink);line-height:1}
.brand .name{font-size:29px;letter-spacing:1px;display:block}
.brand .tag{font-size:9.5px;letter-spacing:4.6px;display:block;margin-top:7px;padding-left:12px}
.brand.light{color:var(--white)}
.heading{position:absolute;font-family:"Michroma",sans-serif;color:var(--ink);font-size:36px;letter-spacing:1px;line-height:1;white-space:nowrap}
.copy{font-size:17.5px;line-height:32.3px;color:var(--text);text-align:justify}

/* slide 1 */
.hero-panel{position:absolute;inset:0}
.hero-intro{left:61px;top:200px;font-family:"Michroma",sans-serif;color:var(--white);font-size:21px;letter-spacing:1px}
.hero-title{left:61px;top:250px;font-family:"Michroma",sans-serif;color:var(--white);font-size:37px;line-height:53px;letter-spacing:.5px}

/* slide 2 */
.service{position:absolute;left:471px;width:520px;height:100px}
.service-icon{position:absolute;left:0;top:0;width:108px;height:100px;border:2px solid var(--brand);padding:5px}
.service-icon div{width:100%;height:100%;background:var(--brand);display:flex;align-items:center;justify-content:center}
.service h3{position:absolute;left:132px;top:2px;font-size:24px;font-weight:500;color:#111}
.service p{position:absolute;left:133px;top:40px;width:390px;font-size:17.5px;line-height:32.5px;color:#222}

/* slide 5 */
.pillar{position:absolute;left:60px;width:480px}
.pillar-icon{position:absolute;left:0;width:92px;height:92px;border-radius:50%;display:flex;align-items:center;justify-content:center}
.pillar h3{position:absolute;left:117px;font-size:24px;font-weight:500;color:var(--brand-deep)}
.pillar p{position:absolute;left:117px;width:380px;font-size:17.5px;line-height:32.5px;color:var(--muted)}

/* slide 6 */
.social{position:absolute;top:327px;width:60px;height:57px;border:2px solid var(--white);border-radius:3px}
</style>
</head>
<body>

<!-- Slide 1: Welcome -->
<section class="slide" style="top:97px">
  <div class="photo" role="img" aria-label="Two site engineers in hard hats and high-visibility vests reviewing a tablet beside heavy machinery"
       style="inset:0;clip-path:polygon(575px 0,1034px 0,1034px 580px,272px 580px);background:linear-gradient(135deg,#8c8f93 0%,#d8b93a 35%,#c74a2a 55%,#5b5a58 80%,#3a3836 100%)"></div>
  <svg class="hero-panel" width="1034" height="580" viewBox="0 0 1034 580">
    <polygon points="0,118 600,118 392,538 0,538" fill="var(--brand)"/>
    <line x1="575" y1="0" x2="520" y2="118" stroke="var(--white)" stroke-width="3"/>
    <polygon points="300,560 360,560 372,580 290,580" fill="var(--brand-soft)" opacity=".7"/>
    <line x1="385" y1="468" x2="358" y2="530" stroke="var(--white)" stroke-width="3"/>
    <line x1="405" y1="430" x2="380" y2="488" stroke="var(--white)" stroke-width="2"/>
    <line x1="608" y1="118" x2="390" y2="580" stroke="var(--brand)" stroke-width="4"/>
  </svg>
  <div class="brand" style="left:63px;top:40px"><span class="name">BOREALIS</span><span class="tag">FROSTLINE CONSULTING</span></div>
  <div class="abs hero-intro">WELCOME TO</div>
  <div class="abs hero-title">BOREALIS<br>FROSTLINE<br>CONSULTING.</div>
</section>

<!-- Slide 2: Services -->
<section class="slide" style="top:750px">
  <div class="brand" style="left:61px;top:20px"><span class="name">BOREALIS</span><span class="tag">FROSTLINE CONSULTING</span></div>
  <div class="heading" style="left:600px;top:36px;font-size:34px">OUR SERVICES</div>
  <div class="abs" style="left:19px;top:110px;width:976px;height:455px;border:2px solid var(--brand)"></div>
  <div class="photo" role="img" aria-label="Offshore oil and gas platform on open sea under a cloudy sky"
       style="left:39px;top:86px;width:391px;height:464px;background:linear-gradient(180deg,#b9c6d3 0%,#7d8fa3 30%,#c9a53a 52%,#2d4a63 72%,#1b3046 100%)"></div>
  <div class="service" style="top:148px">
    <div class="service-icon"><div><svg width="48" height="48" viewBox="0 0 48 48" fill="none" stroke="#fff" stroke-width="2"><rect x="6" y="24" width="36" height="18"/><rect x="12" y="12" width="8" height="12"/><rect x="28" y="30" width="8" height="6"/></svg></div></div>
    <h3>Mining</h3>
    <p>Lorem ipsum dolor&nbsp; consectetur adipiscing elited eiusmod tempor incididunt&nbsp; labord.</p>
  </div>
  <div class="service" style="top:292px">
    <div class="service-icon"><div><svg width="48" height="48" viewBox="0 0 48 48" fill="none" stroke="#fff" stroke-width="2"><rect x="6" y="26" width="22" height="12"/><rect x="28" y="30" width="12" height="8"/><circle cx="13" cy="40" r="3"/><circle cx="34" cy="40" r="3"/><line x1="14" y1="12" x2="36" y2="12"/></svg></div></div>
    <h3>Transportation</h3>
    <p>Lorem ipsum dolor&nbsp; consectetur adipiscing elited eiusmod tempor incididunt&nbsp; labord.</p>
  </div>
  <div class="service" style="top:437px">
    <div class="service-icon"><div><svg width="48" height="48" viewBox="0 0 48 48" fill="none" stroke="#fff" stroke-width="2"><rect x="6" y="22" width="36" height="20"/><rect x="10" y="10" width="6" height="12"/><rect x="22" y="28" width="6" height="6"/><rect x="32" y="28" width="6" height="6"/></svg></div></div>
    <h3>Industries</h3>
    <p>Lorem ipsum dolor&nbsp; consectetur adipiscing elited eiusmod tempor incididunt&nbsp; labord.</p>
  </div>
</section>

<!-- Slide 3: Why choose us -->
<section class="slide" style="top:1403px">
  <div class="brand" style="left:61px;top:22px"><span class="name">BOREALIS</span><span class="tag">FROSTLINE CONSULTING</span></div>
  <div class="heading" style="left:63px;top:103px">WHY CHOOSE US</div>
  <svg class="abs" style="inset:0" width="1034" height="580" viewBox="0 0 1034 580">
    <circle cx="1030" cy="290" r="522" fill="none" stroke="#a9c9ea" stroke-width="8"/>
  </svg>
  <div class="photo" role="img" aria-label="Two workers in hard hats and orange safety jackets in front of an industrial processing plant"
       style="left:508px;top:-232px;width:1044px;height:1044px;border-radius:50%;background:linear-gradient(160deg,#b7c5cf 0%,#5f6a6f 35%,#d06a2a 55%,#3c4a5c 75%,#6d6255 100%)"></div>
  <div class="abs" style="left:14px;top:203px;width:120px;height:120px;border-radius:50%;background:#e3edf7"></div>
  <div class="abs copy" style="left:63px;top:238px;width:521px;height:268px;background:#fff;padding:20px 35px;box-shadow:0 8px 26px rgba(0,0,0,.12)">
    Lorem ipsum dolor sit amet, consectetur adipiscing elit, sed do eiusmod tempor incididunt ut labore et dolore magna aliqua. Ut enim ad minim veniam, quis nostrud exercitation ullamco laboris nisi ut aliquip ex commodo consequat Duis aute&nbsp; dolor reprehenderit in voluptate velit esse cillum dolore eu fugiat nulla pariatur. Excepteur sint occaecat cupidatat.
  </div>
</section>

<!-- Slide 4: About us -->
<section class="slide" style="top:2056px">
  <div class="photo" role="img" aria-label="White semi-truck hauling a trailer along a highway at sunset"
       style="left:0;top:0;width:470px;height:580px;background:linear-gradient(110deg,#5b6e7e 0%,#cfd4d8 40%,#e8b35a 70%,#8a6a45 100%)"></div>
  <div class="abs" style="left:0;top:0;width:213px;height:580px;background:var(--brand);opacity:.72"></div>
  <div class="brand" style="left:105px;top:76px"><span class="name">BOREALIS</span><span class="tag">FROSTLINE CONSULTING</span></div>
  <div class="heading" style="left:527px;top:116px">ABOUT US</div>
  <p class="abs copy" style="left:527px;top:174px;width:444px">Lorem ipsum dolor sit amet, consectetur adipiscing elit, sed do eiusmod tempor incididunt ut labore et dolore magna aliqua. Ut enim ad minim veniam, quis nostrud exercitation ullamco laboris nisi ut aliquip ex ea commodo consequat. Duis aute irure dolor in reprehenderit in voluptate velit esse cillum dolore eu fugiat nulla pariatur. Excepteur sint occaecat cupidatat non proident, sunt in culpa qui officia deserunt mollit anim id est laborum.</p>
</section>

<!-- Slide 5: Vision & mission -->
<section class="slide" style="top:2709px">
  <div class="brand" style="left:61px;top:20px"><span class="name">BOREALIS</span><span class="tag">FROSTLINE CONSULTING</span></div>
  <div class="abs" style="left:845px;top:0;width:189px;height:170px;background:var(--panel)"></div>
  <div class="pillar" style="top:0">
    <div class="pillar-icon" style="top:191px;background:var(--brand)"><svg width="46" height="46" viewBox="0 0 46 46" fill="none" stroke="#fff" stroke-width="2.5"><circle cx="23" cy="23" r="18"/><circle cx="23" cy="23" r="11"/><circle cx="23" cy="23" r="4"/></svg></div>
    <h3 style="top:170px">Vision</h3>
    <p style="top:208px">Lorem ipsum dolor sit ameted consectetur adipiscing do eiusmod tempor incididunt ut labore et dolore magna aliquat enim.</p>
  </div>
  <div class="pillar" style="top:0">
    <div class="pillar-icon" style="top:386px;background:#163e6e"><svg width="46" height="46" viewBox="0 0 46 46" fill="none" stroke="#fff" stroke-width="2.5"><line x1="10" y1="22" x2="36" y2="12"/><line x1="23" y1="20" x2="14" y2="38"/><line x1="23" y1="20" x2="32" y2="38"/></svg></div>
    <h3 style="top:364px">Mission</h3>
    <p style="top:402px">Lorem ipsum dolor sit ameted consectetur adipiscing do eiusmod tempor incididunt ut labore et dolore magna aliquat enim.</p>
  </div>
  <div class="abs" style="left:623px;top:146px;width:361px;height:373px;border:3px solid var(--brand)"></div>
  <div class="photo" role="img" aria-label="Offshore drilling rig and a tanker ship on the sea at sunset"
       style="left:601px;top:185px;width:339px;height:310px;background:linear-gradient(180deg,#6e7f92 0%,#b59a7a 45%,#e0a350 60%,#2f4458 100%)"></div>
  <div class="photo" role="img" aria-label="Cargo plane flying over a container terminal with a yellow truck"
       style="left:745px;top:89px;width:223px;height:215px;background:linear-gradient(170deg,#7aa6d1 0%,#c97a4a 45%,#d6a237 70%,#3d4f66 100%);box-shadow:0 0 0 4px #fff"></div>
</section>

<!-- Slide 6: Thank you -->
<section class="slide" style="top:3362px">
  <div class="photo" role="img" aria-label="Two colleagues reviewing a tablet in a warehouse aisle with a worker in a safety vest behind"
       style="inset:0;background:linear-gradient(100deg,#7b6a55 0%,#b9b2a6 35%,#8a97ad 55%,#c6b9a4 80%,#6e6658 100%)"></div>
  <svg class="abs" style="inset:0" width="1034" height="580" viewBox="0 0 1034 580">
    <line x1="438" y1="52" x2="1034" y2="52" stroke="var(--brand)" stroke-width="4"/>
    <polygon points="455,60 1034,60 1034,505 655,505" fill="var(--brand)"/>
    <polygon points="655,505 1034,505 1034,580 700,580" fill="#ffffff" opacity=".85"/>
    <line x1="430" y1="60" x2="640" y2="520" stroke="var(--brand)" stroke-width="3"/>
    <line x1="652" y1="395" x2="692" y2="478" stroke="#fff" stroke-width="3"/>
    <line x1="640" y1="420" x2="670" y2="482" stroke="#fff" stroke-width="2"/>
    <line x1="650" y1="515" x2="1034" y2="515" stroke="var(--brand)" stroke-width="4"/>
  </svg>
  <div class="brand light" style="left:742px;top:166px"><span class="name" style="font-size:27px">BOREALIS</span><span class="tag" style="font-size:9px;letter-spacing:4px">FROSTLINE CONSULTING</span></div>
  <div class="heading" style="right:66px;top:245px;color:#fff">THANK YOU</div>
  <div class="social" style="left:769px"></div>
  <div class="social" style="left:839px"></div>
  <div class="social" style="left:909px"></div>
</section>

</body>
</html>
```